Business Card Design Project

- makeup artist business card

- original and creative

- Elegant design

- Feel free to come out with cool designs but stick to being elegant and attractive

- Design relates to makeup

- includes name, occupation, contact numbers, email, website

- regular size business card

- round corner card

- double sided

- on 1 side it should just have the website name in the center " browsandblush.example "

Industry/Entity Type

Business

Requirements
Must have
• Marla Voss
Makeup Artist
USA: +1 (415)872-6410
Singapore: +65 83027715
marlavoss@browsandblush.example
www.browsandblush.example
Should not have
• nothing cartoon looking.
Pictures of makeup being grab from the internet.. Examples: eyes or lips.

```html
<!DOCTYPE html>
<html lang="en">
<head>
<meta charset="utf-8">
<title>Marla Voss — Makeup Artist Business Card</title>
<link rel="stylesheet" href="https://fonts.googleapis.com/css2?family=Allura&family=Mrs+Saint+Delafield&family=Open+Sans:wght@400;600&display=swap">
<style>
  :root {
    --backdrop: #f3f3f3;
    --card-white: #f4f2ef;
    --card-black: #141414;
    --ink: #111111;
    --ink-light: #f2f2f2;
    --art-teal: #3aa6a6;
    --art-plum: #7d5a86;
    --art-rose: #e89bb5;
    --art-blush: #f6c8d4;
    --art-gold: #e9c46a;
    --art-slate: #4b5a78;
  }
  * { box-sizing: border-box; margin: 0; padding: 0; }
  html, body {
    width: 1200px;
    height: 1200px;
    overflow: hidden;
    background: var(--backdrop);
  }
  .canvas {
    width: 1200px;
    height: 1200px;
    display: flex;
    flex-direction: column;
    align-items: center;
    justify-content: center;
    gap: 56px;
  }
  .card {
    position: relative;
    width: 900px;
    height: 514px;
    border-radius: 26px;
    overflow: hidden;
    box-shadow: 0 10px 30px rgba(0, 0, 0, 0.18);
  }

  /* Back side */
  .card--back {
    background: var(--card-black);
    display: flex;
    align-items: center;
    justify-content: center;
  }
  .card__website-script {
    font-family: "Mrs Saint Delafield", cursive;
    font-size: 72px;
    color: var(--ink-light);
    letter-spacing: 1px;
  }

  /* Front side */
  .card--front {
    background: var(--card-white);
  }
  .card__artwork {
    position: absolute;
    left: -120px;
    top: -60px;
    width: 560px;
    height: 640px;
    border-radius: 0 62% 48% 0 / 0 55% 60% 0;
    background:
      radial-gradient(circle at 42% 50%, var(--art-teal) 0 60px, transparent 110px),
      radial-gradient(circle at 70% 78%, var(--art-blush) 0 80px, transparent 190px),
      radial-gradient(circle at 35% 20%, var(--art-gold) 0 30px, transparent 120px),
      linear-gradient(160deg, var(--art-slate) 0%, var(--art-plum) 40%, var(--art-rose) 75%, var(--art-blush) 100%);
    opacity: 0.92;
  }
  .card__identity {
    position: absolute;
    right: 150px;
    top: 150px;
    text-align: right;
  }
  .card__name {
    font-family: "Allura", cursive;
    font-size: 96px;
    line-height: 1;
    color: var(--ink);
    font-weight: 400;
  }
  .card__role {
    font-family: "Open Sans", sans-serif;
    font-size: 22px;
    font-weight: 600;
    letter-spacing: 0.5px;
    color: var(--ink);
    margin-top: -4px;
    margin-right: 6px;
  }
  .card__contacts {
    position: absolute;
    right: 56px;
    bottom: 42px;
    text-align: right;
    list-style: none;
    font-family: "Open Sans", sans-serif;
    font-size: 25px;
    line-height: 1.3;
    color: var(--ink);
  }
</style>
</head>
<body>
  <main class="canvas">
    <section class="card card--back" aria-label="Card back">
      <p class="card__website-script">www.browsandblush.example</p>
    </section>

    <section class="card card--front" aria-label="Card front">
      <div class="card__artwork" role="img" aria-label="Painterly pastel illustration of an eye in teal, plum, rose and blush tones"></div>
      <div class="card__identity">
        <h1 class="card__name">Marla Voss</h1>
        <p class="card__role">MAKEUP ARTIST</p>
      </div>
      <ul class="card__contacts">
        <li>USA: +1 (415)872-6410</li>
        <li>Singapore: +65 83027715</li>
        <li>marlavoss@browsandblush.example</li>
        <li>www.browsandblush.example</li>
      </ul>
    </section>
  </main>
</body>
</html>
```